Forge Joiners
Welder Certification
Forge Joiners - Engineering
Creative Brief
Simple
Martin Coleby
QA Manager / SCWI
48217 W 63rd Pl Aurora, CO 80019
martin@forgejoiners.example
forgejoiners.example

```html
<!DOCTYPE html>
<html lang="en">
<head>
<meta charset="utf-8">
<title>Forge Joiners – Business Card</title>
<link rel="stylesheet" href="https://fonts.googleapis.com/css2?family=Michroma&family=Roboto:wght@400;500&display=swap">
<style>
  :root{
    --backdrop:#3b332e;
    --card:#1f2225;
    --card-back:#17191b;
    --orange:#f7a21b;
    --orange-deep:#e2561a;
    --silver-light:#e6e8ea;
    --silver-mid:#a9adb2;
    --silver-dark:#6e7378;
    --text-soft:#c9ccd0;
    --text-muted:#8d9297;
    --text-on-silver:#2a2d30;
  }
  *{margin:0;padding:0;box-sizing:border-box}
  html,body{width:1200px;height:769px;overflow:hidden;background:var(--backdrop)}
  .stage{position:relative;width:1200px;height:769px}

  .card{position:absolute;top:236px;width:520px;height:297px;background:var(--card);
        border-radius:4px;box-shadow:0 10px 30px rgba(0,0,0,.45);overflow:hidden}
  .card--front{left:50px}
  .card--back{left:630px;background:var(--card-back)}

  .brand{position:absolute;left:36px;top:44px;display:flex;align-items:center;gap:12px}
  .brand__mark{width:22px;height:22px;background:var(--orange)}
  .brand__name{font-family:"Michroma",sans-serif;font-size:24px;color:var(--orange);letter-spacing:1px;line-height:1}

  .person{position:absolute;left:36px;top:134px}
  .person__name{font-family:"Michroma",sans-serif;font-size:17px;font-weight:400;color:var(--orange);letter-spacing:1px;line-height:22px}
  .person__role{font-family:"Roboto",sans-serif;font-size:14px;color:var(--text-soft);margin-top:4px}

  .address{position:absolute;left:36px;top:196px;font-family:"Roboto",sans-serif;font-style:normal;font-size:13px;line-height:17px;color:var(--text-muted)}

  .contacts{position:absolute;left:250px;top:162px;font-family:"Roboto",sans-serif;font-size:13px;line-height:20px;color:var(--text-soft);list-style:none}
  .contacts li{display:flex;align-items:center;gap:8px}
  .contacts svg{width:11px;height:11px;flex:none}
  .icon--phone{fill:var(--orange)}
  .icon--mail{fill:var(--orange)}

  .footer{position:absolute;left:0;bottom:0;width:520px;height:60px}
  .footer__url{position:absolute;right:14px;bottom:20px;font-family:"Roboto",sans-serif;font-size:11px;letter-spacing:1.5px;line-height:14px;color:var(--text-on-silver);font-weight:500;white-space:nowrap}

  .back__name{position:absolute;left:0;right:0;top:112px;text-align:center;font-family:"Michroma",sans-serif;font-size:26px;color:var(--silver-mid);letter-spacing:2px}
  .back__url{position:absolute;left:0;right:0;top:190px;text-align:center;font-family:"Roboto",sans-serif;font-size:11px;letter-spacing:4px;color:#3a3d40}
</style>
</head>
<body>
<main class="stage">
  <section class="card card--front">
    <div class="brand">
      <span class="brand__mark"></span>
      <span class="brand__name">FORGE JOINERS</span>
    </div>

    <div class="person">
      <h1 class="person__name">MARTIN COLEBY</h1>
      <p class="person__role">QA Manager / SCWI</p>
    </div>

    <address class="address">48217 W 63rd Pl<br>Aurora, CO 80019</address>

    <ul class="contacts">
      <li><svg class="icon--phone" viewBox="0 0 24 24"><path d="M6.6 10.8a15.1 15.1 0 0 0 6.6 6.6l2.2-2.2c.3-.3.7-.4 1-.2 1.1.4 2.3.6 3.6.6.6 0 1 .4 1 1V20c0 .6-.4 1-1 1A17 17 0 0 1 3 4c0-.6.4-1 1-1h3.5c.6 0 1 .4 1 1 0 1.3.2 2.5.6 3.6.1.3 0 .7-.2 1z"/></svg>720-555-0148</li>
      <li><svg class="icon--mail" viewBox="0 0 24 24"><path d="M2 5h20v2.2l-10 6.5L2 7.2zM2 9.6l10 6.5 10-6.5V19H2z"/></svg>martin@forgejoiners.example</li>
    </ul>

    <svg class="footer" viewBox="0 0 520 60" aria-hidden="true">
      <defs>
        <linearGradient id="stripe-orange" x1="0" x2="1">
          <stop offset="0" stop-color="#f7a21b"/>
          <stop offset="1" stop-color="#e2561a"/>
        </linearGradient>
        <linearGradient id="band-silver" x1="0" y1="0" x2="0" y2="1">
          <stop offset="0" stop-color="#e6e8ea"/>
          <stop offset=".6" stop-color="#a9adb2"/>
          <stop offset="1" stop-color="#6e7378"/>
        </linearGradient>
      </defs>
      <polygon points="0,45 268,45 262,51 0,51" fill="url(#stripe-orange)"/>
      <polygon points="0,54 270,54 308,16 520,16 520,60 0,60" fill="url(#band-silver)"/>
    </svg>
    <span class="footer__url">WWW.FORGEJOINERS.EXAMPLE</span>
  </section>

  <section class="card card--back">
    <p class="back__name">FORGE JOINERS</p>
    <p class="back__url">WWW.FORGEJOINERS.EXAMPLE</p>
  </section>
</main>
</body>
</html>
```